New Plumbing Company

We are looking for a smart and creative business card design for our new plumbing company. We are looking for creativity and originality in our business cards.

Industry/Entity Type

Plumbing

Contact Information for Business Card

Crestline Plumbing
Peter Halvane
Managing Director
Telephone Number : 0481529604
Email : service@crestlineplumbing.com.au
Website : www.crestlineplumbing.com.au
Lic. 508264K

Colors
0692cd
33a6d7
000000

Requirements
Must have
• I want the business card to be designed on a black background using the blue tones i have selected as seen in the company logo.

```html
<!DOCTYPE html>
<html lang="en">
<head>
<meta charset="utf-8">
<title>Crestline Plumbing – Business Card</title>
<link rel="stylesheet" href="https://fonts.googleapis.com/css2?family=Josefin+Sans:wght@300;400;600;700&display=swap">
<style>
  :root {
    --page-bg: #eeeeee;
    --card-dark: #141414;
    --card-mid: #2b2b2b;
    --photo-dark: #1c1c1c;
    --photo-light: #3a3a3a;
    --strip: #363636;
    --blue: #4f7fbf;
    --blue-light: #6a93cc;
    --blue-fold: #34609c;
    --text-light: #ffffff;
    --text-soft: #dcdcdc;
  }
  * { margin: 0; padding: 0; box-sizing: border-box; }
  html, body {
    width: 1200px; height: 1107px; overflow: hidden;
    background: var(--page-bg);
    font-family: "Josefin Sans", sans-serif;
  }
  .business-card {
    position: absolute; left: 100px; top: 268px;
    width: 1000px; height: 572px; overflow: hidden;
    background: radial-gradient(ellipse at 65% 35%, var(--card-mid) 0%, var(--card-dark) 75%);
    box-shadow: 0 18px 40px rgba(0,0,0,0.25);
  }
  .photo-panel {
    position: absolute; left: 0; top: 0; width: 422px; height: 517px;
    background: linear-gradient(160deg, var(--photo-light) 0%, var(--photo-dark) 70%);
  }
  .logo-band {
    position: absolute; left: 0; top: 96px; width: 422px; height: 176px;
    background: rgba(255,255,255,0.07);
    display: flex; align-items: center; gap: 16px; padding-left: 22px;
  }
  .logo-dot {
    width: 96px; height: 96px; border-radius: 50%;
    border: 5px solid var(--blue); flex: none;
  }
  .brand-name { color: var(--text-light); font-weight: 400; line-height: 1; }
  .brand-name .brand-main { display: block; font-size: 50px; }
  .brand-name .brand-sub { display: block; font-size: 20px; letter-spacing: 6px; margin-top: 8px; text-align: center; }
  .banner {
    position: absolute; right: 31px;
    background: var(--blue-light);
    clip-path: polygon(8% 0, 100% 0, 100% 100%, 0 100%);
    display: flex; align-items: center; justify-content: flex-end;
    padding-right: 6px; color: var(--text-light);
  }
  .name-banner { top: 162px; width: 334px; height: 47px; }
  .person-name { font-size: 37px; font-weight: 600; letter-spacing: 1px; padding-top: 6px; }
  .job-title {
    position: absolute; right: 33px; top: 214px;
    font-size: 23px; font-weight: 300; color: var(--text-soft);
  }
  .phone-banner { top: 254px; width: 454px; height: 49px; clip-path: polygon(7% 0, 100% 0, 100% 100%, 0 100%); }
  .phone-label { font-size: 24px; font-weight: 300; padding-top: 5px; }
  .phone-number { font-size: 30px; font-weight: 600; padding-top: 5px; margin-left: 6px; }
  .email-line {
    position: absolute; right: 31px; top: 310px;
    color: var(--text-light); white-space: nowrap;
  }
  .email-label { font-size: 23px; font-weight: 300; }
  .email-address { font-size: 26px; font-weight: 600; letter-spacing: 0.5px; }
  .bottom-strip {
    position: absolute; left: 0; top: 517px; width: 1000px; height: 55px;
    background: var(--strip);
  }
  .web-tab {
    position: absolute; left: 269px; top: 500px; width: 497px; height: 72px;
    background: var(--blue);
    text-align: center; color: var(--text-light);
  }
  .web-fold { position: absolute; top: 500px; }
  .web-fold.left { left: 253px; }
  .web-fold.right { left: 766px; }
  .website { display: block; font-size: 28px; font-weight: 700; letter-spacing: 1px; padding-top: 13px; }
  .licence { display: block; font-size: 17px; font-weight: 400; margin-top: 1px; }
</style>
</head>
<body>
  <div class="business-card">
    <div class="photo-panel" role="img" aria-label="Dim photograph of pipes and fittings under a sink"></div>
    <div class="logo-band">
      <div class="logo-dot"></div>
      <div class="brand-name">
        <span class="brand-main">Crestline</span>
        <span class="brand-sub">Plumbing</span>
      </div>
    </div>

    <div class="banner name-banner"><span class="person-name">Peter Halvane</span></div>
    <div class="job-title">Managing Director</div>

    <div class="banner phone-banner">
      <span class="phone-label">Telephone Number :</span>
      <span class="phone-number">0481529604</span>
    </div>

    <div class="email-line">
      <span class="email-label">Email : </span>
      <span class="email-address">service@crestlineplumbing.com.au</span>
    </div>

    <div class="bottom-strip"></div>
    <svg class="web-fold left" width="16" height="17" viewBox="0 0 16 17"><polygon points="0,0 16,0 16,17" fill="var(--blue-fold)"/></svg>
    <svg class="web-fold right" width="16" height="17" viewBox="0 0 16 17"><polygon points="0,0 16,0 0,17" fill="var(--blue-fold)"/></svg>
    <div class="web-tab">
      <span class="website">www.crestlineplumbing.com.au</span>
      <span class="licence">Lic. 508264K</span>
    </div>
  </div>
</body>
</html>
```